Advertisment for hair care product

We are a company that distributes hair smoothing products. We are planning an advertising campaign to introduce the product in the local market (product website is velmorisilk.com).

The advertisement will be displayed on the back of the buses (see details of sizes in attached photos) in Kuwait city. The goal of the advert is to attract customers to try the product and alleviate their fears of safety. We have hired a model to user her pictures for the add (please see fylebarn link to raw images below).

The text of the adverts will be on the following (We have not chosen yet):

1) Very effective. Really safe.
2) Really smooth hair. No need to worry.
3) Smooth hair now. Healthy hair for the future.
4) Your hair, back to its health before dying it.
5) Why use blow dry everyday?

In general, we really like Corvelle adverts and lunavique.

The advert should also make it clear that this product is licensed by the health authorities in Kuwait. It is one of the very few products that passed the rigorous testing by the health authorities in Kuwait.

I uploaded a banner that we designed in the past to show you what I liked. Please use this as a data point. I am looking for something fresh and completely different. You can take the logo and other things from it.

For this product, we had a model in a photo shoot session. The pictures can be found in this folder.
https://www.fylebarn.com/sh/qrtxwmvbhzpe8da/BBKpQzRytLx3mFnoWsDjHtEbP?dl=0

Target Market(s)

Our target market is women generally in the age 18-60. Our goal is to motivate them enough to talk to their salons to use our products.

Industry/Entity Type

Hair

Requirements
Must have
• 1) Small text as mentioned in the brief
• 2) We have to show the product images
• 3) An indication that the product is approved by Kuwait's Bureau of Wellness Oversight
• 4) Please note that the final design will be translated in Arabic. Please make sure that your design takes into account the right-to-left nature of the Arabic language. Your design can be in English, but have to be designed as right-to-left.
Nice to have
• Text in Arabic:
• 1) صج ينعم. وايد آمن
• 2) شعر ناعم من غير ما تحاتين
• 3) نعومة فورية وصحة دايمة
• 4) صحة شعري رجعت مثل قبل ما أصبغة
• 5) ارتحت من السشوار كل يوم

```html
<!DOCTYPE html>
<html lang="en">
<head>
<meta charset="utf-8">
<title>Smooth Hair Now – Bus Back Advertisement</title>
<link rel="stylesheet" href="https://fonts.googleapis.com/css2?family=Exo+2:ital,wght@0,300;0,700;1,300;1,700;1,800&family=Tajawal:wght@400;500&display=swap">
<style>
  :root {
    --green-deep: #3d9e2c;
    --green-mid: #4fb53a;
    --green-light: #66c94c;
    --ink-white: #ffffff;
    --photo-dark: #2b2624;
    --photo-mid: #4a3d36;
    --photo-warm: #7a604f;
    --bottle-white: #f4f5f3;
    --bottle-shade: #d9dcd8;
  }
  * { margin: 0; padding: 0; box-sizing: border-box; }
  html, body { width: 1200px; height: 1069px; overflow: hidden; }
  body {
    position: relative;
    background: radial-gradient(ellipse at 60% 45%, var(--green-light) 0%, var(--green-mid) 55%, var(--green-deep) 100%);
    font-family: "Exo 2", sans-serif;
    color: var(--ink-white);
  }
  .model-photo {
    position: absolute;
    left: 0; top: 96px;
    width: 520px; height: 973px;
    border-radius: 24px 24px 0 0;
    background: linear-gradient(180deg, var(--photo-warm) 0%, var(--photo-mid) 40%, var(--photo-dark) 100%);
  }
  .headline { position: absolute; text-align: right; line-height: 1; white-space: nowrap; }
  .headline-smooth { top: 114px; right: 184px; font-weight: 300; font-style: italic; font-size: 78px; }
  .headline-now { top: 162px; right: 178px; font-weight: 800; font-style: italic; font-size: 226px; letter-spacing: -4px; }
  .headline-healthy { top: 366px; right: 222px; font-weight: 300; font-style: italic; font-size: 76px; }
  .headline-future { top: 436px; right: 222px; font-weight: 700; font-style: italic; font-size: 64px; }
  .headline-rule {
    position: absolute; left: 480px; top: 502px;
    width: 496px; height: 2px; background: var(--ink-white);
  }
  .headline-arabic {
    position: absolute; right: 222px; top: 510px;
    direction: rtl; font-family: "Tajawal", sans-serif; font-weight: 500;
    font-size: 46px; line-height: 1.1; white-space: nowrap;
  }
  .claims { position: absolute; right: 310px; text-align: right; white-space: nowrap; }
  .claim-tested { top: 704px; font-weight: 300; font-style: italic; font-size: 23px; line-height: 28px; }
  .claim-approved { top: 768px; font-weight: 700; font-style: italic; font-size: 23px; line-height: 28px; }
  .claim-arabic {
    top: 858px; direction: rtl; font-family: "Tajawal", sans-serif;
    font-size: 22px; line-height: 34px;
  }
  .bracket { position: absolute; left: 896px; top: 640px; }
  .product-bottle { position: absolute; left: 916px; top: 644px; width: 108px; height: 304px; }
</style>
</head>
<body>
  <div class="model-photo" role="img" aria-label="Photograph of the model with long flowing brown hair in a black blazer and white blouse"></div>

  <div class="headline headline-smooth">SMOOTH HAIR</div>
  <div class="headline headline-now">NOW</div>
  <div class="headline headline-healthy">HEALTHY HAIR</div>
  <div class="headline headline-future">FOR THE FUTURE</div>
  <div class="headline-rule"></div>
  <div class="headline-arabic">نعومة فورية وصحة دايمة</div>

  <svg class="bracket" width="60" height="250" viewBox="0 0 60 250" aria-hidden="true">
    <g fill="none" stroke="#ffffff" stroke-width="2">
      <line x1="8" y1="8" x2="8" y2="234"/>
      <line x1="8" y1="8" x2="50" y2="8"/>
    </g>
    <g fill="#ffffff">
      <rect x="43" y="3" width="10" height="10"/>
      <rect x="3" y="73" width="10" height="10"/>
      <rect x="3" y="137" width="10" height="10"/>
      <rect x="3" y="229" width="10" height="10"/>
    </g>
  </svg>

  <div class="claims claim-tested">RIGOROUSLY TESTED<br>AND PROVEN</div>
  <div class="claims claim-approved">APPROVED KUWAIT<br>HEALTH AUTHORITY<br>PRODUCT</div>
  <div class="claims claim-arabic">وافقت الكويت هيئة الصحة<br>المنتج</div>

  <svg class="product-bottle" role="img" aria-label="White bottle of smoothing treatment product" viewBox="0 0 108 304">
    <defs>
      <linearGradient id="bottleTone" x1="0" y1="0" x2="1" y2="0">
        <stop offset="0" stop-color="#d9dcd8"/>
        <stop offset="0.4" stop-color="#f4f5f3"/>
        <stop offset="1" stop-color="#d9dcd8"/>
      </linearGradient>
    </defs>
    <rect x="30" y="0" width="48" height="34" rx="4" fill="url(#bottleTone)"/>
    <path d="M10 46 Q10 34 24 34 L84 34 Q98 34 98 46 L98 294 Q98 304 88 304 L20 304 Q10 304 10 294 Z" fill="url(#bottleTone)"/>
  </svg>
</body>
</html>
```